Quimby's Yard & Garden Center Business Card Update

I need an updated Business card design for my Lawn and Garden Center. We do Landscaping installs, Lawn Mowing, Snow Removal and also have a Garden Center Retail Division. I uploaded a few of our previous business cards to give an idea of what we are starting with. The main goal of this update is to simplify and modernize the business card, not all of the services that are on the previous cards has to be on the new one but I would still like to highlight our main services. There is also a sample of our logo that Can be used in the design.

Industry/Entity Type

Landscaping

Contact Information for Business Card

Morris Quimby
Morris@Quimbysyardandgarden.example
Business (555) 201-7784
Cell (555) 318-6092

Colors

Designer to choose colors to be used in the design.

Requirements
Must have
• Services Provided :
• Landscaping
• Lawn Maintenance
• Snow Removal
• Garden Center

```html
<!DOCTYPE html>
<html lang="en">
<head>
<meta charset="utf-8">
<title>Quimby's Yard &amp; Garden Center – Business Card</title>
<link rel="stylesheet" href="https://fonts.googleapis.com/css2?family=Source+Serif+4:wght@400;700&family=PT+Sans+Narrow&display=swap">
<style>
  :root {
    --green: #2d5a2a;
    --ink: #2b2b2b;
    --panel: rgba(255, 255, 255, 0.82);
    --page: #ffffff;
  }
  * { box-sizing: border-box; margin: 0; padding: 0; }
  html, body { width: 1200px; height: 1200px; overflow: hidden; background: var(--page); }
  .canvas { position: relative; width: 1200px; height: 1200px; }

  .card {
    position: absolute;
    top: 179px;
    width: 482px;
    height: 840px;
    overflow: hidden;
  }
  .card--front { left: 81px; }
  .card--back { left: 630px; }

  .flower-photo {
    position: absolute;
    inset: 0;
    background:
      radial-gradient(circle at 20% 6%, #f2c919 0 40px, transparent 70px),
      radial-gradient(circle at 70% 8%, #e9b91a 0 45px, transparent 80px),
      radial-gradient(circle at 92% 30%, #d2521c 0 40px, transparent 90px),
      radial-gradient(circle at 6% 40%, #c6481a 0 50px, transparent 100px),
      radial-gradient(circle at 10% 75%, #b8441a 0 50px, transparent 110px),
      radial-gradient(circle at 95% 80%, #c24a18 0 40px, transparent 100px),
      radial-gradient(circle at 50% 97%, #e3b21c 0 40px, transparent 90px),
      radial-gradient(circle at 6% 57%, #8c7fd0 0 14px, transparent 30px),
      linear-gradient(180deg, #6f8a35 0%, #8a7a2c 35%, #7b5a26 65%, #6d7a33 100%);
  }

  .panel {
    position: absolute;
    left: 59px;
    width: 365px;
    background: var(--panel);
    border: 3px solid var(--green);
    text-align: center;
  }
  .card--front .panel { top: 50px; height: 743px; }
  .card--back .panel { top: 211px; height: 570px; }

  .line {
    position: absolute;
    left: 0;
    right: 0;
    white-space: nowrap;
  }

  .brand-name {
    font-family: "Source Serif 4", serif;
    font-weight: 700;
    color: var(--green);
    font-size: 48px;
    line-height: 60px;
  }
  .brand-mark {
    display: inline-block;
    width: 22px;
    height: 22px;
    border-radius: 50%;
    background: var(--green);
    margin-right: 12px;
    vertical-align: middle;
  }

  .tagline {
    font-family: "Source Serif 4", serif;
    font-weight: 700;
    font-size: 17px;
    line-height: 22px;
    color: var(--green);
  }
  .person {
    font-family: "Source Serif 4", serif;
    font-weight: 700;
    font-size: 32px;
    line-height: 40px;
    color: var(--green);
  }
  .contact {
    font-family: "PT Sans Narrow", sans-serif;
    font-size: 18.5px;
    line-height: 24px;
    color: var(--ink);
  }
  .address {
    font-family: "Source Serif 4", serif;
    font-size: 21px;
    line-height: 26px;
    color: var(--ink);
  }
  .website {
    font-family: "Source Serif 4", serif;
    font-weight: 700;
    font-size: 20px;
    line-height: 28px;
    color: var(--green);
  }

  .services {
    font-family: "Source Serif 4", serif;
    font-size: 23px;
    line-height: 30px;
    color: var(--ink);
  }
  .services .bullet {
    display: inline-block;
    width: 9px;
    height: 9px;
    border-radius: 50%;
    background: var(--green);
    margin-right: 10px;
    vertical-align: 5px;
  }
  .back-contact {
    font-family: "Source Serif 4", serif;
    font-weight: 700;
    font-size: 19.5px;
    line-height: 26px;
    color: var(--green);
  }

  .back-brand {
    position: absolute;
    left: 0;
    right: 0;
    top: 95px;
    text-align: center;
    font-family: "Source Serif 4", serif;
    font-weight: 700;
    font-size: 44px;
    line-height: 56px;
    color: #ffffff;
  }
  .back-brand .brand-mark { background: #ffffff; }
</style>
</head>
<body>
<main class="canvas">

  <section class="card card--front">
    <div class="flower-photo" role="img" aria-label="Close-up photo of a garden bed of yellow and orange coneflowers with purple blooms"></div>
    <div class="panel">
      <div class="line brand-name" style="top:80px;"><span class="brand-mark"></span>Quimby's</div>
      <div class="line tagline" style="top:205px;">YARD AND GARDEN CENTER</div>
      <div class="line person" style="top:308px;">Morris Quimby</div>
      <div class="line contact" style="top:454px;">Morris@Quimbysyardandgarden.example</div>
      <div class="line contact" style="top:490px;">Business (555) 201-7784</div>
      <div class="line contact" style="top:527px;">Cell (555) 318-6092</div>
      <div class="line address" style="top:592px;">2280 County Road K,</div>
      <div class="line address" style="top:624px;">Millbrook, Ohio 45500</div>
      <div class="line website" style="top:683px;">quimbysyardandgarden.example</div>
    </div>
  </section>

  <section class="card card--back">
    <div class="flower-photo" role="img" aria-label="Close-up photo of a garden bed of yellow and orange coneflowers with purple blooms"></div>
    <div class="back-brand"><span class="brand-mark"></span>Quimby's</div>
    <div class="panel">
      <div class="line services" style="top:31px;"><span class="bullet"></span>Landscaping</div>
      <div class="line services" style="top:75px;"><span class="bullet"></span>Lawn Maintenance</div>
      <div class="line services" style="top:118px;"><span class="bullet"></span>Snow Removal</div>
      <div class="line services" style="top:161px;"><span class="bullet"></span>Garden Center</div>
      <div class="line services" style="top:204px;"><span class="bullet"></span>Annuals, Perennials,</div>
      <div class="line services" style="top:241px;">Trees, Shrubs</div>
      <div class="line services" style="top:284px;"><span class="bullet"></span>Garden, Pond &amp;</div>
      <div class="line services" style="top:321px;">Landscaping Supplies</div>
      <div class="line services" style="top:364px;"><span class="bullet"></span>Full Service Fresh</div>
      <div class="line services" style="top:401px;">Floral Department</div>
      <div class="line back-contact" style="top:490px;">Business (555) 201-7784</div>
      <div class="line back-contact" style="top:517px;">quimbysyardandgarden.example</div>
    </div>
  </section>

</main>
</body>
</html>
```